A poster for Vale Chiropractic's up coming powerful health workshop/seminar

I need a poster developed for Dr. Pruitt's upcoming Lasting Body Renewal and Armor Plating your Wellness seminar/workshop. This workshop will teach attendants how to shed pounds and rapidly reduce their waist size. Learn why weight loss doesn't work 99.9% of the time so that you can be the successful .1%. It's time to expose the LIES and reveal the TRUTH about the REAL causes of HEART DISEASE, DIABETES, CANCER, CHRONIC FATIGUE, ARTHRITIS, FIBROMYALGIA, and how to REVERSE/PREVENT this from ever happening to you or your family. The Insider Secrets to building your body into a health fortress unbreachable by sickness and disease. Learn to live and fufill your GOD-GIVEN health potential. Eliminate high bloodpressure, high cholesterol, diabetes, fatigue, chronic pain
Ending the WAR on sickness and disease by launching an unstoppable health offensive that will pummel any enemy of life and health.

I'm not a designer by any means, but was thinking of possible WAR theme, cammo, etc....just a thought. Not a requirement by any means
Updates

Dr. Pruitt has taken a look at all the submissions and has requested a few changes.

1. He wants the new map that has been added to the brief with Millbrook Valley College as a title above the map

2. He wants a section that describes what the attendees will gain at the seminar in bullet format.  Example:  Title....It's not about what you lose

                                                   I'ts about what you gain....

>The No-Hype, No- Gimmick  secrets for fast effective Weight loss

>How the top 3 disease killers, heart disease, cancer, and diabetes are linked to diet

>Tools and strategies to make 2012 the best year ever

The Seminar will be held at Millbrook Valley College, Tuesday January 3rd @ 6:30pm Open to Public

Target Market(s)

Adults 30-65

Industry/Entity Type

Building

Requirements
Should not have
• ruyrtur

```html
<!DOCTYPE html>
<html lang="en">
<head>
<meta charset="utf-8">
<title>Ending the War on Sickness &amp; Desease – Seminar Poster</title>
<link rel="stylesheet" href="https://fonts.googleapis.com/css2?family=Montserrat:wght@800;900&family=Questrial&display=swap">
<style>
  :root {
    --poster-purple: #c94fd8;
    --panel-pink: rgba(244, 214, 246, 0.9);
    --skin-light: #f2c9a8;
    --skin-mid: #e7b08c;
    --skin-shade: #b98468;
    --ink-dark: #2b1f2c;
    --white: #ffffff;
    --photo-dark: #3a2a24;
    --photo-mid: #7a5a4c;
  }
  * { margin: 0; padding: 0; box-sizing: border-box; }
  html, body { width: 1200px; height: 849px; overflow: hidden; background: var(--poster-purple); }
  .poster {
    position: relative;
    width: 1200px;
    height: 849px;
    background: var(--poster-purple);
    overflow: hidden;
    font-family: "Questrial", "Century Gothic", sans-serif;
    color: var(--white);
  }
  .torso-art {
    position: absolute;
    top: 0; right: 0;
    width: 540px; height: 849px;
  }
  .presenter-name {
    position: absolute;
    left: 50px; top: 16px;
    font-size: 38px;
    letter-spacing: 0.5px;
  }
  .headline {
    position: absolute;
    left: 42px; top: 58px;
    font-family: "Montserrat", "Arial Black", sans-serif;
    font-weight: 900;
    font-size: 62px;
    line-height: 1;
    letter-spacing: 0.5px;
  }
  .subhead {
    position: absolute;
    left: 44px; top: 120px;
    font-size: 50px;
    line-height: 1.1;
    padding-bottom: 4px;
    border-bottom: 3px solid var(--white);
    width: 624px;
  }
  .tagline {
    position: absolute;
    left: 50px; top: 191px;
    font-size: 23px;
  }
  .gain-list {
    position: absolute;
    left: 40px; top: 230px;
    list-style: none;
    width: 640px;
  }
  .gain-list li {
    position: relative;
    padding-left: 42px;
    line-height: 1.18;
  }
  .gain-list .star {
    position: absolute;
    left: 0; top: 4px;
    width: 30px; height: 30px;
  }
  .gain-primary { font-size: 27px; margin-bottom: 22px; }
  .gain-secondary { font-size: 20px; margin-bottom: 23px; }
  .gain-secondary .star { width: 26px; height: 26px; top: 0; }
  .gain-tertiary { font-size: 21px; }
  .gain-tertiary .star { width: 26px; height: 26px; top: 0; }
  .venue-panel {
    position: absolute;
    left: 31px; top: 463px;
    width: 604px; height: 271px;
    background: var(--panel-pink);
    border-radius: 28px;
    color: var(--ink-dark);
  }
  .venue-title {
    position: absolute;
    left: 62px; top: 38px;
    font-size: 31px;
  }
  .venue-map {
    position: absolute;
    left: 26px; top: 71px;
    width: 200px; height: 154px;
    background: linear-gradient(135deg, #8f9a86, #6f7c6c 50%, #a4a89c);
  }
  .venue-details {
    position: absolute;
    left: 237px; top: 88px;
    font-size: 24px;
    line-height: 46px;
  }
  .presenter-photo {
    position: absolute;
    left: 637px; top: 516px;
    width: 300px; height: 284px;
    background: var(--white);
    padding: 20px 20px 34px;
    box-shadow: 2px 3px 8px rgba(0,0,0,0.35);
  }
  .presenter-photo .photo-fill {
    width: 100%; height: 100%;
    background: linear-gradient(160deg, var(--photo-mid), var(--photo-dark));
  }
</style>
</head>
<body>
<main class="poster">
  <svg class="torso-art" role="img" aria-label="Illustration of a bare torso with a yellow tape measure around the waist" viewBox="0 0 540 849" preserveAspectRatio="none">
    <defs>
      <linearGradient id="skinTone" x1="0" y1="0" x2="1" y2="0">
        <stop offset="0" stop-color="var(--skin-mid)"/>
        <stop offset="0.5" stop-color="var(--skin-light)"/>
        <stop offset="1" stop-color="var(--skin-mid)"/>
      </linearGradient>
    </defs>
    <path d="M40 0 H540 V849 H90 C60 700 70 560 120 430 C150 330 90 180 40 0 Z" fill="url(#skinTone)"/>
  </svg>

  <p class="presenter-name">Dr Pruitt’s</p>
  <h1 class="headline">ENDING THE WAR</h1>
  <h2 class="subhead">on Sickness &amp; Desease</h2>
  <p class="tagline">It's not about what you lose its about what you gain.</p>

  <ul class="gain-list">
    <li class="gain-primary">
      <svg class="star" viewBox="0 0 24 24" aria-hidden="true"><path fill="var(--white)" d="M12 1.5l3.1 6.9 7.4.7-5.6 5 1.7 7.4L12 17.7l-6.6 3.8 1.7-7.4-5.6-5 7.4-.7z"/></svg>
      How the top 3 disease killers, heart disease, cancer, and diabetes are linked to diet.
    </li>
    <li class="gain-secondary">
      <svg class="star" viewBox="0 0 24 24" aria-hidden="true"><path fill="var(--white)" d="M12 1.5l3.1 6.9 7.4.7-5.6 5 1.7 7.4L12 17.7l-6.6 3.8 1.7-7.4-5.6-5 7.4-.7z"/></svg>
      The No-Hype, No- Gimmick&nbsp; secrets for fast effective weight loss.
    </li>
    <li class="gain-tertiary">
      <svg class="star" viewBox="0 0 24 24" aria-hidden="true"><path fill="var(--white)" d="M12 1.5l3.1 6.9 7.4.7-5.6 5 1.7 7.4L12 17.7l-6.6 3.8 1.7-7.4-5.6-5 7.4-.7z"/></svg>
      Tools and strategies to make 2012 the best year ever.
    </li>
  </ul>

  <section class="venue-panel">
    <p class="venue-title">The Seminar will be held at:</p>
    <div class="venue-map" role="img" aria-label="Aerial map of the college campus with the auditorium marked"></div>
    <p class="venue-details">
      Millbrook Valley College,<br>
      Tuesday January 3rd @ 6:30pm<br>
      Open to Public
    </p>
  </section>

  <figure class="presenter-photo">
    <div class="photo-fill" role="img" aria-label="Portrait photo of Dr. Pruitt in a dark suit"></div>
  </figure>
</main>
</body>
</html>
```